Lantern Cove Summer Camps Banner Ads

Seeking to create 6 banner ads (two variations of 3 banner sizes. 1) 250x250 2)468x60 3)120x600.
We are a Spanish and French immersion summer camp based in Chapel Hill, North Carolina. You can view our website at http://lanterncove-example.org
We've included our logo attached, colors should be reflective of branded colors in the logo.
Our target market is the South East, United State (FL, GA, NC, SC, TN, VA). Parents (focus on mothers) with kids from grades 1-12 (ages 5-17).
Our calls to action are to register/sign up for camps, and explore our website (Goal is clicks not views).
Language for ad: English.
Final design should be a fun, family-centric ad, which encapsulates the user and encourages them to learn more about Lantern Cove. Preferably, ad can be used ever-green for reuse in different seasons (does not contain date restrictions, for example ad should NOT contain "Join us for Summer Camp 2018").
Typical tag lines include: Friends, languages and a lot of fun! All the fun of a summer camp while totally immersed in the language and culture!
Target Market(s)

```html
<!DOCTYPE html>
<html lang="en">
<head>
<meta charset="utf-8">
<title>Lantern Cove Summer Camps – Banner Ads</title>
<link rel="stylesheet" href="https://fonts.googleapis.com/css2?family=Montserrat:wght@400;500;600;700;800;900&display=swap">
<style>
  :root {
    --stage: #c0c0c0;
    --camp-green: #0a8f77;
    --camp-green-deep: #077a66;
    --sky-top: #b9e3f6;
    --sky-bottom: #ffffff;
    --brand-blue: #1d78bd;
    --headline-cream: #fff2b3;
    --white: #ffffff;
    --cta-yellow: #fbb812;
    --cta-text: #2a2a2a;
    --photo-light: #9fb58a;
    --photo-dark: #4d6a45;
  }
  * { box-sizing: border-box; margin: 0; padding: 0; }
  html, body { width: 1200px; height: 1103px; overflow: hidden; }
  body {
    background: var(--stage);
    font-family: "Montserrat", Arial, sans-serif;
    position: relative;
  }
  .banner {
    position: absolute;
    overflow: hidden;
    background: var(--camp-green);
    color: var(--white);
    transform-origin: 0 0;
    transform: scale(1.6713);
  }
  .banner--skyscraper { left: 42px; top: 48px; width: 160px; height: 600px; }
  .banner--square { left: 359px; top: 48px; width: 250px; height: 250px; }
  .banner--leaderboard { left: 359px; top: 516px; width: 468px; height: 60px; }

  .sky { position: absolute; left: 0; top: 0; }
  .brand-name {
    position: absolute;
    color: var(--brand-blue);
    font-weight: 700;
    white-space: nowrap;
    letter-spacing: 0.2px;
  }
  .kicker { position: absolute; font-weight: 500; text-transform: uppercase; text-align: center; line-height: 1.15; }
  .headline {
    position: absolute;
    color: var(--headline-cream);
    font-weight: 900;
    text-transform: uppercase;
    letter-spacing: -0.5px;
    line-height: 0.95;
    text-align: center;
  }
  .body-copy { position: absolute; font-weight: 400; line-height: 1.3; }
  .cta {
    position: absolute;
    display: flex; align-items: center; justify-content: center;
    background: var(--cta-yellow);
    color: var(--cta-text);
    font-weight: 700;
    border-radius: 999px;
    white-space: nowrap;
  }
  .site-url { position: absolute; font-weight: 400; letter-spacing: 0.2px; white-space: nowrap; }
  .photo-fill { fill: url(#photoTone); }

  /* Skyscraper */
  .banner--skyscraper .sky { width: 160px; height: 100px; }
  .banner--skyscraper .brand-name { left: 0; width: 160px; text-align: center; top: 52px; font-size: 16px; }
  .banner--skyscraper .kicker { left: 0; width: 160px; top: 114px; font-size: 14px; }
  .banner--skyscraper .headline { left: 0; width: 160px; top: 158px; font-size: 49px; line-height: 0.96; }
  .banner--skyscraper .body-copy { left: 6px; width: 148px; top: 301px; font-size: 10.5px; text-align: center; }
  .banner--skyscraper .cta { left: 18px; top: 364px; width: 125px; height: 29px; font-size: 12px; }
  .banner--skyscraper .site-url { left: 0; width: 160px; text-align: center; top: 399px; font-size: 9.5px; }
  .banner--skyscraper .photo { position: absolute; left: 0; top: 424px; }

  /* Square */
  .banner--square .sky { width: 250px; height: 80px; }
  .banner--square .brand-name { left: 0; width: 250px; text-align: center; top: 46px; font-size: 17px; }
  .banner--square .kicker { left: 0; width: 250px; top: 85px; font-size: 13px; }
  .banner--square .headline { left: 0; width: 250px; top: 101px; font-size: 29.5px; }
  .banner--square .body-copy { left: 10px; width: 150px; top: 141px; font-size: 10.5px; text-align: center; }
  .banner--square .cta { left: 16px; top: 192px; width: 124px; height: 28px; font-size: 12px; }
  .banner--square .site-url { left: 12px; top: 228px; font-size: 9px; }
  .banner--square .photo {
    position: absolute; left: 154px; top: 137px; width: 122px; height: 122px;
    border-radius: 50%; border: 4px solid var(--white);
    background: linear-gradient(160deg, var(--photo-light), var(--photo-dark));
  }

  /* Leaderboard */
  .banner--leaderboard .sky { width: 140px; height: 60px; }
  .banner--leaderboard .brand-name { left: 0; width: 130px; text-align: center; top: 32px; font-size: 12px; }
  .banner--leaderboard .kicker { left: 140px; width: 186px; top: 5px; font-size: 11px; }
  .banner--leaderboard .headline { left: 140px; width: 186px; top: 18px; font-size: 22px; }
  .banner--leaderboard .body-copy { left: 140px; width: 186px; top: 41px; font-size: 9.5px; text-align: center; }
  .banner--leaderboard .photo {
    position: absolute; left: 330px; top: -42px; width: 210px; height: 150px;
    border-radius: 50%; border: 3px solid var(--white);
    background: linear-gradient(160deg, var(--photo-light), var(--photo-dark));
  }
  .banner--leaderboard .cta { left: 344px; top: 31px; width: 118px; height: 23px; font-size: 11px; }
</style>
</head>
<body>
<svg width="0" height="0" style="position:absolute" aria-hidden="true">
  <defs>
    <linearGradient id="skyTone" x1="0" y1="0" x2="0" y2="1">
      <stop offset="0" stop-color="#b9e3f6"/>
      <stop offset="1" stop-color="#ffffff"/>
    </linearGradient>
    <linearGradient id="skyToneSide" x1="0" y1="0" x2="1" y2="0">
      <stop offset="0" stop-color="#b9e3f6"/>
      <stop offset="1" stop-color="#ffffff"/>
    </linearGradient>
    <linearGradient id="photoTone" x1="0" y1="0" x2="1" y2="1">
      <stop offset="0" stop-color="#9fb58a"/>
      <stop offset="1" stop-color="#4d6a45"/>
    </linearGradient>
  </defs>
</svg>

<section class="banner banner--skyscraper" aria-label="Lantern Cove 160 by 600 banner">
  <svg class="sky" viewBox="0 0 160 100" aria-hidden="true">
    <path d="M0 0H160V88C130 100 110 80 80 90C50 100 30 82 0 92Z" fill="url(#skyTone)"/>
  </svg>
  <p class="brand-name">Lantern Cove</p>
  <p class="kicker">Friends,<br>Languages &amp;</p>
  <h2 class="headline">Lots<br>of<br>Fun!</h2>
  <p class="body-copy">Join the fun camp while totally immersed in the language &amp; culture!</p>
  <a class="cta">Schedule Here!</a>
  <p class="site-url">www.lanterncove-example.org</p>
  <svg class="photo" width="160" height="176" viewBox="0 0 160 176" role="img" aria-label="Photo of campers jumping together on a forest trail">
    <path class="photo-fill" d="M0 32C40 -4 120 -4 160 32V176H0Z" stroke="#ffffff" stroke-width="4"/>
  </svg>
</section>

<section class="banner banner--square" aria-label="Lantern Cove 250 by 250 banner">
  <svg class="sky" viewBox="0 0 250 80" aria-hidden="true">
    <path d="M0 0H250V70C205 80 170 60 125 70C80 80 45 62 0 72Z" fill="url(#skyTone)"/>
  </svg>
  <p class="brand-name">Lantern Cove</p>
  <p class="kicker">Friends, Languages &amp;</p>
  <h2 class="headline">Lots of Fun!</h2>
  <p class="body-copy">Join the fun camp while totally immersed in the language &amp; culture!</p>
  <a class="cta">Schedule Here!</a>
  <p class="site-url">www.lanterncove-example.org</p>
  <div class="photo" role="img" aria-label="Photo of campers jumping together outdoors"></div>
</section>

<section class="banner banner--leaderboard" aria-label="Lantern Cove 468 by 60 banner">
  <svg class="sky" viewBox="0 0 140 60" aria-hidden="true">
    <path d="M0 0H134C128 15 140 30 132 45C128 52 134 56 136 60H0Z" fill="url(#skyToneSide)"/>
  </svg>
  <p class="brand-name">Lantern Cove</p>
  <p class="kicker">Friends, Languages &amp;</p>
  <h2 class="headline">Lots of Fun!</h2>
  <p class="body-copy">Join our fun and exciting camp!!</p>
  <div class="photo" role="img" aria-label="Photo of campers jumping together outdoors"></div>
  <a class="cta">Schedule Here!</a>
</section>
</body>
</html>
```